Large Wall sticker for gym that's creative, colourful and eye catching

I'm wanting a sticker which takes up the whole wall to put up in my gym. Colourful, eye catching & inspiring.
Something people want to take a photo in front of
Possibly a black back ground, anything to do with gym/fitness as images.

My gyms name is Zenpro Health & Fitness 24/7
Logo colours are white, navy blue, yellow and black but happy for other colours to be used.

I had an idea of some sort of Grafitti writing - just something colourful that pops.

Slogans that could be used-
Reach your potential
Built not bought.
(Both don't need to be used)

Hi guys, the wall is 5m Long 3m tall.

I'm wanting something gym/fitness related. Not just the words built not bought.

Some sort of image/quote that makes people feel inspired when they walk past it.

Industry/Entity Type

Fitness / gym

Requirements
Must have
• Colour.
Nice to have
• Colour, something eye catching, an inspiring wall that people want to take a photo in front of.

```html
<!DOCTYPE html>
<html lang="en">
<head>
<meta charset="utf-8">
<title>Reach Your Potential – Gym Wall Mural</title>
<link href="https://fonts.googleapis.com/css2?family=Bangers&display=swap" rel="stylesheet">
<style>
  :root {
    --blue-deep: #0d2a9e;
    --blue-bright: #1f6fe0;
    --orange: #f47a1c;
    --orange-light: #ffb030;
    --red: #e8321e;
    --yellow: #ffd23a;
    --white: #ffffff;
    --charcoal: #1c1c22;
    --page: #e9e9e9;
  }
  * { margin: 0; padding: 0; box-sizing: border-box; }
  html, body {
    width: 1200px;
    height: 675px;
    overflow: hidden;
    background: var(--page);
  }
  .mural {
    position: relative;
    width: 1200px;
    height: 675px;
    overflow: hidden;
  }
  .mural__burst {
    position: absolute;
    inset: 0;
    background:
      radial-gradient(circle at 58% 50%, var(--yellow) 0%, var(--orange-light) 12%, transparent 34%),
      linear-gradient(135deg, var(--red) 0%, var(--orange) 22%, var(--blue-bright) 45%, var(--blue-deep) 62%, var(--orange) 82%, var(--red) 100%);
  }
  .mural__athlete {
    position: absolute;
    left: 714px;
    top: 0;
    width: 332px;
    height: 675px;
    background: linear-gradient(180deg, #3a3030 0%, #262224 45%, var(--charcoal) 100%);
    border-radius: 120px 120px 0 0;
    opacity: 0.92;
  }
  .mural__slogan {
    position: absolute;
    left: 18px;
    top: 96px;
    font-family: "Bangers", "Impact", sans-serif;
    font-size: 172px;
    line-height: 0.93;
    letter-spacing: 2px;
    text-transform: uppercase;
  }
  .slogan__line {
    display: block;
    color: var(--red);
    background: linear-gradient(180deg, var(--red) 0%, var(--orange) 55%, var(--orange-light) 100%);
    -webkit-background-clip: text;
    background-clip: text;
    -webkit-text-fill-color: transparent;
    -webkit-text-stroke: 7px var(--white);
    paint-order: stroke fill;
  }
</style>
</head>
<body>
  <main class="mural">
    <div class="mural__burst" role="img" aria-label="Sunburst background of orange, red and blue rays over low-poly shapes"></div>
    <div class="mural__athlete" role="img" aria-label="Photo of a muscular athlete in a black tank top doing a cable curl"></div>
    <h1 class="mural__slogan">
      <span class="slogan__line">Reach</span>
      <span class="slogan__line">Your</span>
      <span class="slogan__line">Potential</span>
    </h1>
  </main>
</body>
</html>
```